Business Card Design Project

We are a consulting company which works with tourism operators and attractions, wineries, heritage sites, National and conservation parks etc to help them identify their 'Point of Difference' and then deliver an exceptional tourism visitor experience.
We specialise in: Operator training, Site interpretation, Product and experience development, Planning and analysis.
We have a tag line of "Shaping every visit - truly well."
The company name is MoxVerse and the logo is this word with the 'Mox' in black and the 'Verse' in orange - but this can be changed. The 'a' is a speech bubble. A lot of what we do involves talking!
The design should communicate that we can make a big difference to the range and quality of experiences that visitors get at your site.
Updates

I put the wrong telephone number in my brief. My apologies.

It should be +61 0481 902 317

Target Market(s)

tourism busineses, wineries and cellar doors, heritage sites, environment managers, Government agencies & private companies

Industry/Entity Type

Tourism

Requirements
Must have
• Name: Corin Hollis
Title: Emeritus Professor
Qualifications: BSc(Hons), PhD
Role: Director
Address: PO Box 318, Larkhaven, Coral Coast 6132
Phone: (+61) 0481 902 317
Email: corin@moxverse-example.com.au
www.moxverse-example.com.au
ABN 871 204 519 36

Operator Training, Site Interpretation, Product and Experience Development, Planning and Analysis.
Nice to have
• Awards:
Winner 2011 SA Voyager Honours – Kestrel Polytechnic - Tourism Education and Training
Winner 2009 SA Voyager Honours - Outstanding Contribution by an Individual
Winner 2009 Gulfland Citizen Medal - Tourism Award
Should not have
• No 'shadows' to company name/logo please.
No black reverse side of card

```html
<!DOCTYPE html>
<html lang="en">
<head>
<meta charset="utf-8">
<title>MoxVerse Consulting – Business Card</title>
<link rel="stylesheet" href="https://fonts.googleapis.com/css2?family=Arimo:wght@400;700&family=Carlito:wght@400;700&display=swap">
<style>
  :root {
    --orange: #d2731c;
    --ink: #1a1a1a;
    --grey-text: #555555;
    --grey-band: #a3a3a3;
    --paper: #ffffff;
    --backdrop: #e6e6e6;
  }
  * { box-sizing: border-box; margin: 0; padding: 0; }
  html, body { width: 1200px; height: 800px; overflow: hidden; }
  body {
    background: var(--backdrop);
    position: relative;
    font-family: "Carlito", "Calibri", sans-serif;
    color: var(--ink);
  }
  .card {
    position: absolute;
    top: 230px;
    width: 560px;
    height: 340px;
    background: var(--paper);
    overflow: hidden;
  }
  .card--front { left: 25px; }
  .card--back { left: 615px; font-family: "Arimo", "Arial", sans-serif; }

  /* Shared wordmark */
  .wordmark {
    font-family: "Carlito", "Calibri", sans-serif;
    font-weight: 700;
    color: var(--ink);
    display: flex;
    align-items: center;
    gap: 8px;
    line-height: 1;
  }
  .wordmark__dot {
    width: 12px; height: 12px;
    border-radius: 50%;
    background: var(--orange);
  }

  /* Front */
  .card--front .wordmark {
    position: absolute;
    left: 40px; top: 104px;
    font-size: 46px;
  }
  .person {
    position: absolute;
    right: 34px; top: 30px;
    text-align: right;
  }
  .person__name { font-size: 22px; font-weight: 700; letter-spacing: 0.5px; }
  .person__title { font-size: 15px; margin-top: 2px; }
  .person__quals { font-size: 14px; color: var(--orange); margin-top: 2px; }
  .contact {
    position: absolute;
    right: 34px; top: 150px;
    text-align: right;
    font-size: 14px;
    line-height: 1.4;
  }
  .contact__label { color: var(--orange); font-weight: 700; }
  .contact__address { margin-top: 10px; }
  .contact__abn { margin-top: 10px; color: var(--grey-text); }
  .website {
    position: absolute;
    left: 0; right: 0; bottom: 26px;
    text-align: center;
    font-size: 16px;
  }
  .website__name { color: var(--orange); font-weight: 700; }

  /* Back */
  .card--back .wordmark {
    position: absolute;
    left: 36px; top: 30px;
    font-size: 40px;
  }
  .tagline {
    position: absolute;
    left: 38px; top: 82px;
    font-size: 14px;
    color: var(--grey-text);
  }
  .awards {
    position: absolute;
    left: 0; right: 0; top: 120px;
    height: 86px;
    background: var(--orange);
    display: flex;
    align-items: center;
    padding: 0 16px 0 22px;
    gap: 16px;
  }
  .awards::after {
    content: "";
    position: absolute;
    left: 0; right: 0; bottom: -10px;
    height: 10px;
    background: var(--grey-band);
  }
  .awards__badge {
    flex: 0 0 52px;
    height: 52px;
    border-radius: 50%;
    background: #f3d9bf;
  }
  .awards__list {
    list-style: none;
    color: var(--paper);
    font-size: 10px;
    line-height: 1.55;
  }
  .awards__win { font-weight: 700; }
  .services {
    position: absolute;
    left: 36px; right: 24px; top: 234px;
    list-style: none;
    display: grid;
    grid-template-columns: 1fr 1fr;
    row-gap: 16px;
    column-gap: 14px;
    font-size: 13px;
    line-height: 1.2;
    letter-spacing: 0.3px;
    text-transform: uppercase;
  }
  .services__item { display: flex; align-items: center; gap: 10px; }
  .services__icon { flex: 0 0 16px; width: 16px; height: 14px; }
</style>
</head>
<body>

<section class="card card--front" aria-label="Card front">
  <div class="wordmark"><span>MoxVerse</span><span class="wordmark__dot"></span></div>

  <div class="person">
    <div class="person__name">CORIN HOLLIS</div>
    <div class="person__title">Emeritus Professor</div>
    <div class="person__quals">Qualifications: BSc(Hons), PhD</div>
  </div>

  <div class="contact">
    <div><span class="contact__label">Phone:</span> +61 0481 902 317</div>
    <div><span class="contact__label">Email:</span> corin@moxverse-example.com.au</div>
    <div class="contact__address">PO Box 318, Larkhaven<br>Coral Coast 6132</div>
    <div class="contact__abn">ABN 871 204 519 36</div>
  </div>

  <div class="website">www.<span class="website__name">moxverse-example</span>.com.au</div>
</section>

<section class="card card--back" aria-label="Card back">
  <div class="wordmark"><span>MoxVerse</span><span class="wordmark__dot"></span></div>
  <div class="tagline">Shaping every visit - truly well.</div>

  <div class="awards">
    <div class="awards__badge" role="img" aria-label="Award badge"></div>
    <ul class="awards__list">
      <li><span class="awards__win">WINNER</span> 2011 SA Voyager Honours – Kestrel Polytechnic – Tourism Education and Training</li>
      <li><span class="awards__win">WINNER</span> 2009 SA Voyager Honours – Outstanding Contribution by an Individual</li>
      <li><span class="awards__win">WINNER</span> 2009 Gulfland Citizen Medal – Tourism Award</li>
    </ul>
  </div>

  <ul class="services">
    <li class="services__item">
      <svg class="services__icon" viewBox="0 0 16 14" aria-hidden="true"><path d="M2 0h12a2 2 0 0 1 2 2v6a2 2 0 0 1-2 2H7l-4 4v-4H2a2 2 0 0 1-2-2V2a2 2 0 0 1 2-2z" fill="var(--orange)"/></svg>
      Operator Training
    </li>
    <li class="services__item">
      <svg class="services__icon" viewBox="0 0 16 14" aria-hidden="true"><path d="M2 0h12a2 2 0 0 1 2 2v6a2 2 0 0 1-2 2H7l-4 4v-4H2a2 2 0 0 1-2-2V2a2 2 0 0 1 2-2z" fill="var(--orange)"/></svg>
      Site Interpretation
    </li>
    <li class="services__item">
      <svg class="services__icon" viewBox="0 0 16 14" aria-hidden="true"><path d="M2 0h12a2 2 0 0 1 2 2v6a2 2 0 0 1-2 2H7l-4 4v-4H2a2 2 0 0 1-2-2V2a2 2 0 0 1 2-2z" fill="var(--orange)"/></svg>
      Product and Experience Development
    </li>
    <li class="services__item">
      <svg class="services__icon" viewBox="0 0 16 14" aria-hidden="true"><path d="M2 0h12a2 2 0 0 1 2 2v6a2 2 0 0 1-2 2H7l-4 4v-4H2a2 2 0 0 1-2-2V2a2 2 0 0 1 2-2z" fill="var(--orange)"/></svg>
      Planning and Analysis
    </li>
  </ul>
</section>

</body>
</html>
```